3 fold Flyer Design (A4)

We are offering a good value, professional, Search Engine Optimisation package which is being offered with a 'free' entry onto a local web site. and need to advertise the benefits within a 3 fold flyer. The content may change to show the name of a differen local website (e.g. www.harrowmeadlive.com . The design must look exciting, this is a great offer!

We have attached a draft of the content to the brief. A new brief has been atached 05/01/2011
Updates

Reason: Having viewed the existing designs we feel a need for change to a more dynamic 'sales' approach

Having reviewd the designs we decided to change our approah to make the brochure more sales led than professional.
To compensate for this we have increased the budget a little.
We have also added new text and improved the brief.
Thanks

Target Market(s)

business owners in the North West. Mostly private businesses from shops to manufacturing. Mostly in competitive markets.

Industry/Entity Type

It Professional

Requirements
Must have
• Bright fresh approach which gets over the benefit of increasing business. Happy and positive, with the concept of success.

The Rupert vane Internet logo added to the back page small in size. (attached)
Nice to have
• design which gives the reader confidence to buy
Should not have
• Boring pictures

```html
<!DOCTYPE html>
<html lang="en">
<head>
<meta charset="utf-8">
<title>Tri-fold Flyer – Business Foundation SEO Package</title>
<link rel="stylesheet" href="https://fonts.googleapis.com/css2?family=Arimo:wght@400;700&family=Nunito:wght@600;800&display=swap">
<style>
  :root{
    --stage:#3b3b3d;
    --purple:#5c2a87;
    --purple-deep:#47206c;
    --purple-soft:#74409e;
    --lime:#c9e43a;
    --orange:#f6921e;
    --sky:#29a8e0;
    --green:#8dc63f;
    --star:#fcd920;
    --white:#ffffff;
    --paper:#fbfbfb;
    --body-font:"Arimo", Arial, sans-serif;
    --display-font:"Nunito", Arial, sans-serif;
  }
  *{box-sizing:border-box;margin:0;padding:0}
  html,body{width:1200px;height:900px;overflow:hidden}
  body{background:var(--stage);font-family:var(--body-font);color:var(--white);position:relative}

  .sheet{position:absolute;top:40px;height:820px;display:flex;box-shadow:0 6px 18px rgba(0,0,0,.45)}
  .sheet--outside{left:24px;width:452px}
  .sheet--inside{left:496px;width:680px;background:var(--purple);
    background-image:repeating-linear-gradient(135deg,rgba(255,255,255,.035) 0 2px,transparent 2px 9px)}

  /* ---------- cover ---------- */
  .cover{width:226px;height:100%;position:relative;overflow:hidden;background:var(--purple);
    background-image:repeating-linear-gradient(135deg,rgba(255,255,255,.035) 0 2px,transparent 2px 9px)}
  .cover__bands{position:absolute;left:0;top:0;width:226px;height:150px}
  .cover__photo{position:absolute;left:0;top:150px;width:226px;height:230px;
    background:linear-gradient(160deg,#e9eef2 0%,#c8ccd0 45%,#6e6a70 100%)}
  .cover__headline{position:absolute;left:14px;right:10px;top:400px;font-family:var(--display-font);
    font-weight:800;line-height:1.02;text-align:right}
  .cover__headline span{display:block}
  .hl-small{font-size:21px;color:var(--white)}
  .hl-sky{font-size:27px;color:var(--sky)}
  .hl-green{font-size:33px;color:var(--green)}
  .hl-orange{color:var(--orange)}
  .cover__offer{position:absolute;right:12px;top:565px;font-size:9px;font-style:italic;color:var(--white)}
  .cover__star{position:absolute;left:6px;top:610px;width:100px;height:100px}
  .cover__star-text{position:absolute;left:6px;top:610px;width:100px;height:100px;display:flex;
    align-items:center;justify-content:center;text-align:center;font-family:var(--display-font);
    font-weight:800;font-size:14px;line-height:1.05;color:var(--purple-deep);transform:rotate(-12deg)}
  .cover__pitch{position:absolute;left:110px;right:10px;top:618px;font-size:8.5px;font-weight:700;
    line-height:1.3;text-align:right;color:var(--white)}
  .cover__pitch em{color:var(--star);font-style:normal}
  .cover__pitch p+p{margin-top:8px;color:var(--lime)}

  /* ---------- back ---------- */
  .back{width:226px;height:100%;background:var(--paper);position:relative}
  .brand{position:absolute;right:16px;bottom:24px;display:flex;align-items:center;gap:7px}
  .brand__dot{width:22px;height:22px;border-radius:50%;background:var(--purple)}
  .brand__name{font-family:var(--body-font);font-weight:700;font-size:13px;line-height:1.05;color:var(--purple)}

  /* ---------- inside ---------- */
  .inside-photo{position:absolute;top:0;height:170px}
  .inside-photo--handshake{left:0;width:227px;background:linear-gradient(180deg,#f3f3f5 0%,#c9c9cf 60%,#8a8792 100%)}
  .inside-photo--address{left:227px;width:226px;background:linear-gradient(165deg,#dfe7f1 0%,#9fb3cc 55%,#3d5a86 100%)}
  .panel{position:absolute;padding:0 13px;font-size:8.3px;line-height:1.32}
  .panel--one{left:0;top:182px;width:227px}
  .panel--two{left:227px;top:182px;width:226px}
  .panel--three{left:453px;top:14px;width:227px}
  .offer-band{position:absolute;left:227px;top:598px;width:453px;padding:0 13px;font-size:8.3px;line-height:1.32;
    border-top:1px solid rgba(255,255,255,.18);padding-top:10px}

  .h-orange{font-family:var(--display-font);font-weight:800;color:var(--orange);font-size:15px;margin:10px 0 5px}
  .h-orange:first-child{margin-top:0}
  .h-lime{font-weight:700;color:var(--lime);font-size:10px;line-height:1.2;margin:8px 0 3px}
  .h-lime-sm{font-weight:700;font-style:italic;color:var(--lime);font-size:9.5px;margin:6px 0 2px}
  .panel p,.offer-band p{margin-bottom:5px}
  .bullets{list-style:disc;padding-left:11px;margin-bottom:5px}
  .steps{list-style:none;counter-reset:step}
  .steps li{counter-increment:step;margin-bottom:5px}
  .steps li .h-lime{display:flex;gap:4px;margin-top:4px}
  .steps li .h-lime::before{content:counter(step) ".";flex:none}
  .offer-band .small-print{list-style:disc;padding-left:11px}
</style>
</head>
<body>

<!-- Outside of the flyer: cover and back -->
<section class="sheet sheet--outside">
  <article class="cover">
    <svg class="cover__bands" viewBox="0 0 226 150" aria-hidden="true">
      <polygon points="0,0 226,0 226,40 0,110" fill="#6a3596"/>
      <polygon points="0,0 140,0 0,60" fill="#7a45a6"/>
      <polygon points="226,40 226,150 0,150 0,110" fill="#532679"/>
    </svg>
    <div class="cover__photo" role="img" aria-label="Photo of three smiling business people gathered around a laptop in a bright office"></div>
    <h1 class="cover__headline">
      <span class="hl-small">Would you like to</span>
      <span class="hl-sky">attract more</span>
      <span class="hl-green">customers</span>
      <span class="hl-small">to your <span class="hl-orange">business?</span></span>
    </h1>
    <p class="cover__offer">Special offer for 2011</p>
    <svg class="cover__star" viewBox="0 0 100 100" aria-hidden="true">
      <polygon fill="var(--star)" points="98,50 88.6,60.4 91.6,74 78.3,78.3 74,91.6 60.4,88.6 50,98 39.6,88.6 26,91.6 21.7,78.3 8.4,74 11.4,60.4 2,50 11.4,39.6 8.4,26 21.7,21.7 26,8.4 39.6,11.4 50,2 60.4,11.4 74,8.4 78.3,21.7 91.6,26 88.6,39.6"/>
    </svg>
    <div class="cover__star-text">Buy one<br>get one<br>free!</div>
    <div class="cover__pitch">
      <p>Buy our Business Foundation Search Engine Optimisation package and have a banner advert on <em>'HarrowmeadLive.com'</em> for free!</p>
      <p>Attract more new customers through promoting your website in 2 great ways</p>
    </div>
  </article>

  <article class="back">
    <div class="brand">
      <span class="brand__dot"></span>
      <span class="brand__name">rupert vane<br>internet solutions</span>
    </div>
  </article>
</section>

<!-- Inside spread -->
<section class="sheet sheet--inside">
  <div class="inside-photo inside-photo--handshake" role="img" aria-label="Photo of two business people shaking hands"></div>
  <div class="inside-photo inside-photo--address" role="img" aria-label="Close-up photo of a web address bar on a screen"></div>

  <div class="panel panel--one">
    <h2 class="h-orange">Buy this</h2>
    <h3 class="h-lime">1. Business Foundation Search Engine Optimisation package</h3>
    <p>Take advantage of our Foundation package where you will receive professional Search Engine Optimisation on your web site to improve your visitor numbers. What we do...</p>
    <ul class="bullets">
      <li>Examine current keywords on your web site</li>
      <li>Research keywords being typed into search engines</li>
      <li>Optimise your keywords within your web site for search engines</li>
      <li>Build external links from over 100 of our UK town portal web sites</li>
      <li>Provide you with monthly reports showing your search engine rankings</li>
    </ul>
    <h2 class="h-orange">Get this for FREE!!!</h2>
    <h3 class="h-lime">2. Banner Advertisement on HarrowmeadLive.com</h3>
    <p>HarrowmeadLive.com is a community website packed with great features including local news, weather, what's on, horoscopes and competitions. One of the most popular features of the site is the business directory which is frequently used by visitors to find local businesses. Advertise on HarrowmeadLive.com and attract more sales &amp; enquiries.</p>
    <h2 class="h-orange">Want more information?</h2>
    <h3 class="h-lime-sm">About Our Search Engine Optimisation Packages</h3>
    <h3 class="h-lime">Increase traffic to your website using SEO</h3>
    <p>Search Engine Optimisation (SEO) is the process of improving a website's position in the Search Engines for a relevant keyword. A constant Search Engine process is crucial if you want your web site to be found by search engines and be on page one for your respective keywords.</p>
  </div>

  <div class="panel panel--two">
    <h3 class="h-lime">Improve your branding?</h3>
    <p>SEO will help to drive visitors to your website and open your business up to a whole new market. With over 3 billion searches on Searchly every day, it makes sense for your website to come up on the first page when somebody is looking for your services or product. Our foundation package is a cost effective SEO service that is perfect for the smaller business.</p>
    <h3 class="h-lime-sm">About HarrowmeadLive.com</h3>
    <h3 class="h-lime">HarrowmeadLive.com, great for your branding and attracting new contacts and sales.</h3>
    <p>HarrowmeadLive.com is a local community website, one of a network of local online portals. There are over 100 online town websites which the main towns and cities across the UK. The Onlines have many features from local news, what's on guide, weather forecasts and our popular local business directories. The business directories are a popular feature and are frequently used by visitors as a tool for finding local businesses. Being on our directory listing pages also help your web site improve its search engine ranking with external links from the directories pointing back to your site.</p>
  </div>

  <div class="panel panel--three">
    <h3 class="h-lime">So what exactly do I get?</h3>
    <ol class="steps">
      <li><h3 class="h-lime">Improve your presence throughout the North West</h3>
        <p>You will receive a full page directory on our North West online directories. This includes your logo, contact details and several paragraphs of keyword optimised text with links to your website.</p></li>
      <li><h3 class="h-lime">Generate new business across the UK with Search Engine Optimisation</h3>
        <p>Our Search Engine Optimisation will improve your ranking in the major Search Engines and drive targeted traffic to your website.</p></li>
      <li><h3 class="h-lime">Increased brand exposure</h3>
        <p>Your company branding will be displayed across HarrowmeadLive.com which will be seen by thousands of people each month.</p></li>
      <li><h3 class="h-lime">Enhanced national coverage</h3>
        <p>A full page listing in 'Prime Business Directories' which covers the majority of towns and cities across the UK.</p></li>
      <li><h3 class="h-lime">See your business contacts grow</h3>
        <p>Our link builders will submit an additional 5 links per month to websites with a good page rank.</p></li>
      <li><h3 class="h-lime">Track your return on investment via monthly reports</h3>
        <p>This will track the advancement of Search Engine positions month on month.</p></li>
      <li><h3 class="h-lime">Assess your organisation's progress with a specialist advisor</h3>
        <p>A detailed annual review will include a face to face meeting where your website's performance will be assessed and compared to other organisations in your industry/business sector; this is often the perfect opportunity to develop marketing opportunities for your website.</p></li>
    </ol>
  </div>

  <div class="offer-band">
    <h3 class="h-lime-sm">Great Value for Money</h3>
    <p>We are offering all of the above for only £150 per month, making this one of the most cost effective Internet Marketing packages in the UK. For more information please call Rupert Vane Internet Solutions on 08000 41 73 20 or email info@rupertvane.net</p>
    <h3 class="h-lime-sm">Guarantee</h3>
    <p>We guarantee that the home page of your website will appear in the top ten organic results returned by Searchly/Findr or Quester within the first six months of contract – or your money back!</p>
    <h3 class="h-lime-sm">The Small Print</h3>
    <ul class="small-print">
      <li>Our packages are subject to a 12 month rolling contract which can be cancelled after 12 months, with one month's notice.</li>
      <li>Please note that increased traffic to your website is normally experienced after 3 months. More generic terms take longer.</li>
      <li>All prices exclude VAT</li>
    </ul>
  </div>
</section>

</body>
</html>
```